Playing Cards for Couples

I’d like a design of a deck of cards (standard 52 cards with 2 jokers) specifically for couples. The cards should be quirky, cute and romantic.

```html
<!DOCTYPE html>
<html lang="en">
<head>
<meta charset="utf-8">
<title>Playing Cards for Couples – Aces and Kings</title>
<link rel="stylesheet" href="https://fonts.googleapis.com/css2?family=Antonio:wght@200;300&display=swap">
<style>
  :root {
    --backdrop: #dbcfd8;
    --paper: #ffffff;
    --rose: #e27ca2;
    --slate: #4f4c5c;
  }
  * { margin: 0; padding: 0; box-sizing: border-box; }
  html, body { width: 1200px; height: 820px; overflow: hidden; }
  body { background: var(--backdrop); font-family: "Antonio", "Arial Narrow", sans-serif; }

  .table { position: relative; width: 1200px; height: 820px; }
  .defs { position: absolute; width: 0; height: 0; }

  .card {
    position: absolute;
    width: 225px;
    height: 315px;
    background: var(--paper);
  }
  .card.hearts, .card.diamonds { --suit: var(--rose); }
  .card.spades, .card.clubs   { --suit: var(--slate); }
  .card { --ink: var(--suit); }

  .card.king { background: var(--suit); --ink: var(--paper); }

  .frame {
    position: absolute;
    inset: 9px;
    border: 2px solid var(--ink);
    border-radius: 3px;
  }

  .corner {
    position: absolute;
    width: 20px;
    display: flex;
    flex-direction: column;
    align-items: center;
  }
  .corner.top { left: 17px; top: 16px; }
  .corner.bottom { right: 17px; bottom: 16px; transform: rotate(180deg); }
  .rank {
    font-weight: 300;
    font-size: 38px;
    line-height: 32px;
    height: 32px;
    color: var(--ink);
  }
  .corner svg { width: 15px; height: 15px; margin-top: 5px; fill: var(--ink); }

  .centre-pip {
    position: absolute;
    left: 50%;
    top: 50%;
    width: 56px;
    height: 56px;
    transform: translate(-50%, -50%);
    fill: var(--ink);
  }

  .col-1 { left: 40px; } .col-2 { left: 337px; } .col-3 { left: 633px; } .col-4 { left: 929px; }
  .row-aces { top: 44px; } .row-kings { top: 443px; }
</style>
</head>
<body>
<main class="table">
  <svg class="defs" aria-hidden="true">
    <defs>
      <symbol id="heart" viewBox="0 0 100 100">
        <path d="M50 92C22 75 5 60 5 36C5 19 17 9 30 9C40 9 47 16 50 26C53 16 60 9 70 9C83 9 95 19 95 36C95 60 78 75 50 92Z"/>
      </symbol>
      <symbol id="spade" viewBox="0 0 100 100">
        <path d="M50 3C30 15 10 30 10 55C10 68 19 75 30 75C38 75 44 71 47 66C47 80 42 90 36 97L64 97C58 90 53 80 53 66C56 71 62 75 70 75C81 75 90 68 90 55C90 30 70 15 50 3Z"/>
      </symbol>
      <symbol id="diamond" viewBox="0 0 100 100">
        <path d="M50 1L97 50L50 99L3 50Z"/>
      </symbol>
      <symbol id="club" viewBox="0 0 100 100">
        <circle cx="50" cy="25" r="20"/>
        <circle cx="26" cy="54" r="19"/>
        <circle cx="74" cy="54" r="19"/>
        <path d="M46 40C47 70 44 86 37 98L63 98C56 86 53 70 54 40Z"/>
      </symbol>
    </defs>
  </svg>

  <article class="card ace hearts col-1 row-aces" aria-label="Ace of hearts">
    <div class="frame"></div>
    <div class="corner top"><span class="rank">A</span><svg viewBox="0 0 100 100"><use href="#heart"/></svg></div>
    <svg class="centre-pip" viewBox="0 0 100 100"><use href="#heart"/></svg>
    <div class="corner bottom"><span class="rank">A</span><svg viewBox="0 0 100 100"><use href="#heart"/></svg></div>
  </article>

  <article class="card ace spades col-2 row-aces" aria-label="Ace of spades">
    <div class="frame"></div>
    <div class="corner top"><span class="rank">A</span><svg viewBox="0 0 100 100"><use href="#spade"/></svg></div>
    <svg class="centre-pip" viewBox="0 0 100 100"><use href="#spade"/></svg>
    <div class="corner bottom"><span class="rank">A</span><svg viewBox="0 0 100 100"><use href="#spade"/></svg></div>
  </article>

  <article class="card ace diamonds col-3 row-aces" aria-label="Ace of diamonds">
    <div class="frame"></div>
    <div class="corner top"><span class="rank">A</span><svg viewBox="0 0 100 100"><use href="#diamond"/></svg></div>
    <svg class="centre-pip" viewBox="0 0 100 100"><use href="#diamond"/></svg>
    <div class="corner bottom"><span class="rank">A</span><svg viewBox="0 0 100 100"><use href="#diamond"/></svg></div>
  </article>

  <article class="card ace clubs col-4 row-aces" aria-label="Ace of clubs">
    <div class="frame"></div>
    <div class="corner top"><span class="rank">A</span><svg viewBox="0 0 100 100"><use href="#club"/></svg></div>
    <svg class="centre-pip" viewBox="0 0 100 100"><use href="#club"/></svg>
    <div class="corner bottom"><span class="rank">A</span><svg viewBox="0 0 100 100"><use href="#club"/></svg></div>
  </article>

  <article class="card king hearts col-1 row-kings" aria-label="King of hearts">
    <div class="frame"></div>
    <div class="corner top"><span class="rank">K</span><svg viewBox="0 0 100 100"><use href="#heart"/></svg></div>
    <svg class="centre-pip" viewBox="0 0 100 100"><use href="#heart"/></svg>
    <div class="corner bottom"><span class="rank">K</span><svg viewBox="0 0 100 100"><use href="#heart"/></svg></div>
  </article>

  <article class="card king spades col-2 row-kings" aria-label="King of spades">
    <div class="frame"></div>
    <div class="corner top"><span class="rank">K</span><svg viewBox="0 0 100 100"><use href="#spade"/></svg></div>
    <svg class="centre-pip" viewBox="0 0 100 100"><use href="#spade"/></svg>
    <div class="corner bottom"><span class="rank">K</span><svg viewBox="0 0 100 100"><use href="#spade"/></svg></div>
  </article>

  <article class="card king diamonds col-3 row-kings" aria-label="King of diamonds">
    <div class="frame"></div>
    <div class="corner top"><span class="rank">K</span><svg viewBox="0 0 100 100"><use href="#diamond"/></svg></div>
    <svg class="centre-pip" viewBox="0 0 100 100"><use href="#diamond"/></svg>
    <div class="corner bottom"><span class="rank">K</span><svg viewBox="0 0 100 100"><use href="#diamond"/></svg></div>
  </article>

  <article class="card king clubs col-4 row-kings" aria-label="King of clubs">
    <div class="frame"></div>
    <div class="corner top"><span class="rank">K</span><svg viewBox="0 0 100 100"><use href="#club"/></svg></div>
    <svg class="centre-pip" viewBox="0 0 100 100"><use href="#club"/></svg>
    <div class="corner bottom"><span class="rank">K</span><svg viewBox="0 0 100 100"><use href="#club"/></svg></div>
  </article>
</main>
</body>
</html>
```